Develop a Corporate Identity for CoachLantern

Looking for a
1. Powerpoint Template
2. Stationery / Letterhead
3. Presentation Folder
4. Business Card

Learn more about the company here at [url removed, login to view] The focus of the brand needs to be on the wheel (or a circle in general) regarding both attached logos as we intend to show that we are a complete training solution. The items must also work with BOTH attached logos.

```html
<!DOCTYPE html>
<html lang="en">
<head>
<meta charset="utf-8">
<title>CoachLantern Business Card</title>
<link rel="stylesheet" href="https://fonts.googleapis.com/css2?family=Open+Sans:wght@300;400;600;700&display=swap">
<style>
  :root {
    --orange: #f7941d;
    --charcoal: #3d3d3f;
    --ink: #444446;
    --card: #ffffff;
    --card-shade: #f1f1f1;
    --backdrop: #e6e4e1;
  }
  * { margin: 0; padding: 0; box-sizing: border-box; }
  html, body { width: 1200px; height: 899px; overflow: hidden; }
  body {
    background: var(--backdrop);
    font-family: "Open Sans", Arial, sans-serif;
    color: var(--ink);
    position: relative;
  }
  .card {
    position: absolute;
    width: 600px;
    height: 343px;
    border-radius: 20px;
    background: linear-gradient(160deg, var(--card) 55%, var(--card-shade));
    box-shadow: 0 6px 18px rgba(0,0,0,0.12);
    overflow: hidden;
  }
  .card-front { left: 90px; top: 90px; }
  .card-back { left: 510px; top: 466px; }

  /* front */
  .front-brand {
    position: absolute; left: 0; right: 0; top: 120px;
    display: flex; align-items: center; justify-content: center; gap: 14px;
  }
  .brand-dot {
    width: 58px; height: 58px; border-radius: 50%;
    background: var(--orange);
  }
  .front-name {
    font-size: 50px; font-weight: 300; color: var(--charcoal); letter-spacing: -1px;
  }
  .front-url {
    position: absolute; left: 0; right: 0; top: 212px;
    text-align: center; font-size: 13px; color: var(--charcoal);
  }

  /* back */
  .back-brand {
    position: absolute; left: 36px; top: 44px;
    display: flex; align-items: center; gap: 10px;
  }
  .back-brand .brand-dot { width: 44px; height: 44px; }
  .back-name { font-size: 38px; font-weight: 400; color: var(--charcoal); letter-spacing: -0.5px; }
  .tagline {
    position: absolute; left: 300px; top: 96px;
    font-size: 14px; color: var(--charcoal); letter-spacing: 0.3px;
  }
  .rule { position: absolute; height: 1.5px; background: var(--orange); }
  .rule-top { left: 300px; right: 36px; top: 126px; }
  .rule-name { left: 36px; width: 300px; top: 232px; }
  .address {
    position: absolute; right: 40px; top: 138px;
    font-size: 14px; line-height: 1.3; text-align: right; color: var(--charcoal);
    display: flex; gap: 8px;
  }
  .address svg { margin-top: 2px; flex: none; }
  .person {
    position: absolute; left: 36px; top: 200px;
    display: flex; align-items: baseline; gap: 8px;
  }
  .person-name { font-size: 20px; font-weight: 700; color: var(--charcoal); }
  .person-bar { font-size: 22px; font-weight: 700; color: var(--charcoal); }
  .person-title { font-size: 13px; font-weight: 600; color: var(--orange); }
  .contacts {
    position: absolute; left: 36px; top: 240px; list-style: none;
    font-size: 14px; line-height: 19px; color: var(--charcoal);
  }
  .contacts li { display: flex; align-items: center; gap: 10px; }
  .contacts svg { flex: none; }
  .footer-band { position: absolute; left: 0; bottom: 0; width: 600px; height: 46px; }
</style>
</head>
<body>

<section class="card card-front" aria-label="Business card front">
  <div class="front-brand">
    <span class="brand-dot"></span>
    <span class="front-name">coachlantern</span>
  </div>
  <p class="front-url">www.coachlantern.com</p>
</section>

<section class="card card-back" aria-label="Business card back">
  <div class="back-brand">
    <span class="brand-dot"></span>
    <span class="back-name">CoachLantern</span>
  </div>
  <p class="tagline">learning solutions</p>
  <div class="rule rule-top"></div>

  <div class="address">
    <svg width="14" height="13" viewBox="0 0 14 13"><path d="M7 0 L14 6 H12 V13 H8.5 V9 H5.5 V13 H2 V6 H0 Z" fill="var(--orange)"/></svg>
    <span>4470 Harborview Ln<br>Suite 8, Cape Coral,<br>Florida, United States</span>
  </div>

  <div class="person">
    <span class="person-name">Dana Whitfield</span>
    <span class="person-bar">|</span>
    <span class="person-title">President/CEO</span>
  </div>
  <div class="rule rule-name"></div>

  <ul class="contacts">
    <li><svg width="12" height="12" viewBox="0 0 12 12"><path d="M2 1 L4.5 1 L5.5 3.5 L4 4.5 C4.8 6.3 5.7 7.2 7.5 8 L8.5 6.5 L11 7.5 L11 10 C6 11 1 6 2 1 Z" fill="var(--orange)"/></svg>1 (855) 404-7316</li>
    <li><svg width="12" height="12" viewBox="0 0 12 12"><rect x="1" y="4" width="10" height="7" rx="1" fill="var(--orange)"/><rect x="3" y="1" width="6" height="4" fill="var(--orange)"/></svg>1 (239) 555-0184</li>
    <li><svg width="12" height="12" viewBox="0 0 12 12"><rect x="0.5" y="2.5" width="11" height="7.5" fill="var(--orange)"/><path d="M0.5 2.5 L6 7 L11.5 2.5" stroke="#fff" fill="none"/></svg>info@coachlantern.com</li>
    <li><svg width="12" height="12" viewBox="0 0 12 12"><circle cx="6" cy="6" r="5.5" fill="var(--orange)"/><circle cx="6" cy="6" r="2" fill="none" stroke="#fff" stroke-width="1.2"/></svg>www.coachlantern.com</li>
  </ul>

  <svg class="footer-band" viewBox="0 0 600 46" aria-hidden="true">
    <rect x="0" y="32" width="600" height="14" fill="var(--charcoal)"/>
    <path d="M400 46 V12 Q400 0 414 0 H600 V46 Z" fill="var(--orange)"/>
  </svg>
</section>

</body>
</html>
```